Japanese Rice Food Package Label

- We are launching Japanese food products to the outdoor community.
- Made in Japan
- We will have multiple flavors of rice but want to keep the package label almost the same and only replace the flavor text (e.g., Mixed Rice, Curry Rice, etc)
- We like simple designs inspired by Japan.
- Label size: 105 mm x148 mm
- Our brand: YURATO https://yurato.co/
- Video message: https://www.clipvane.com/share/4b7e19d0a3c65f2e8d1a7b30c9e5f412

```html
<!DOCTYPE html>
<html lang="en">
<head>
<meta charset="utf-8">
<title>YURATO Dried Rice Food – Mixed Rice Label</title>
<link rel="stylesheet" href="https://fonts.googleapis.com/css2?family=Archivo:wght@400;500&display=swap">
<style>
  :root {
    --page: #ececec;
    --paper: #ffffff;
    --sun-red: #e5192f;
    --earth-brown: #7d5503;
    --cream-light: #fbf3e2;
    --cream-mid: #efe0bd;
    --cream-deep: #dcc594;
    --ink: #000000;
    --edge: #d6d6d6;
  }
  * { margin: 0; padding: 0; box-sizing: border-box; }
  html, body {
    width: 1200px;
    height: 682px;
    overflow: hidden;
    background: var(--page);
    font-family: "Archivo", Arial, sans-serif;
  }
  .label {
    position: absolute;
    left: 160px;
    top: 31px;
    width: 880px;
    height: 621px;
    background: var(--paper);
    border: 1px solid var(--edge);
    overflow: hidden;
  }
  .label__sun {
    position: absolute;
    left: 0;
    top: 0;
    width: 880px;
    height: 621px;
  }
  .label__band {
    position: absolute;
    left: 0;
    top: 337px;
    width: 100%;
    height: 284px;
    display: flex;
  }
  .band__cream {
    width: 490px;
    height: 100%;
    background: linear-gradient(90deg, var(--cream-light) 0%, var(--cream-mid) 60%, var(--cream-deep) 100%);
  }
  .band__earth {
    flex: 1;
    background: var(--earth-brown);
    position: relative;
  }
  .brand-name {
    position: absolute;
    right: 32px;
    bottom: 28px;
    font-family: "Archivo", Arial, sans-serif;
    font-size: 40px;
    font-weight: 500;
    line-height: 1;
    color: var(--cream-light);
  }
  .product-box {
    position: absolute;
    left: 36px;
    top: 375px;
    width: 422px;
    height: 214px;
    border: 2px solid var(--ink);
    color: var(--ink);
  }
  .product-box__category {
    height: 43px;
    border-bottom: 2px solid var(--ink);
    padding: 6px 0 0 10px;
    font-size: 27px;
    font-weight: 400;
    line-height: 1;
  }
  .product-box__flavor {
    height: 60px;
    border-bottom: 2px solid var(--ink);
    padding: 5px 0 0 9px;
    font-size: 48px;
    font-weight: 500;
    letter-spacing: -2.5px;
    line-height: 1;
  }
  .product-box__features {
    list-style: none;
    padding: 12px 0 0 20px;
    font-size: 22px;
    line-height: 20px;
  }
  .product-box__features li::before {
    content: "•";
    display: inline-block;
    width: 15px;
  }
</style>
</head>
<body>
  <main class="label">
    <svg class="label__sun" viewBox="0 0 880 621" aria-hidden="true">
      <circle cx="349" cy="285" r="229" fill="var(--sun-red)"/>
    </svg>

    <div class="label__band">
      <div class="band__cream"></div>
      <div class="band__earth">
        <p class="brand-name">YURATO</p>
      </div>
    </div>

    <section class="product-box">
      <p class="product-box__category">Dried Rice Food</p>
      <h1 class="product-box__flavor">Mixed Rice</h1>
      <ul class="product-box__features">
        <li>No Cooking</li>
        <li>Just pour hot water</li>
        <li>15 min</li>
        <li>Long Life</li>
      </ul>
    </section>
  </main>
</body>
</html>
```